Veltora Software Business Card Design

We are a new organization called Veltora. We are a software as a service provider. We deliver a project and program management solution via the internet, so everyone has the ability to work together and collaborate. Its an enterprise platform and we will focus on 50 plus employee company.

We have a website in place
www.veltora-demo.com

Use this as a start of producing the business card. The logo is there as well, but if you have a great and better solution...

Color scheme's could be inline with the website, but don't pin point on it. We can always change the website, logo, color scheme etc.

Target Market(s)

B2B, Projectmembers, projectmanagers, ICT, CTO, Marketing Managers

Industry/Entity Type

Software

Requirements
Must have
• Marten Kuyvelsma

Tel: +31 255 47 09 36
Mob: +31 6 927 15 062
marten@veltora-demo.com
Oostelingpad 84c
2184 KT Lindervaart

Www.veltora-demo.com
social media links

```html
<!DOCTYPE html>
<html lang="en">
<head>
<meta charset="utf-8">
<title>Veltora Business Card</title>
<link rel="stylesheet" href="https://fonts.googleapis.com/css2?family=Questrial&display=swap">
<style>
  :root {
    --backdrop: #e8e7eb;
    --card-white: #f7f8f9;
    --lime: #9db31b;
    --lime-light: #adc11a;
    --olive-dark: #5b6a0a;
    --band-grey: #d3d4d6;
    --ink: #555759;
    --ink-soft: #66686a;
  }
  * { box-sizing: border-box; margin: 0; padding: 0; }
  html, body {
    width: 1200px; height: 934px; overflow: hidden;
    background: var(--backdrop);
    font-family: "Questrial", "Century Gothic", sans-serif;
  }
  .stage { position: relative; width: 1200px; height: 934px; }
  .card {
    position: absolute; top: 307px;
    width: 520px; height: 320px;
    box-shadow: 0 6px 18px rgba(0,0,0,0.12);
    overflow: hidden;
  }
  .card-back {
    left: 60px;
    background: linear-gradient(100deg, var(--lime-light) 0%, #8fa314 45%, var(--olive-dark) 100%);
    display: flex; align-items: center; justify-content: center;
  }
  .card-back .wordmark { font-size: 54px; color: #fff; letter-spacing: 1px; }
  .card-front { left: 620px; background: var(--card-white); }
  .brand-band {
    position: absolute; left: 0; top: 128px;
    width: 282px; height: 58px; background: var(--lime);
    display: flex; align-items: center; padding-left: 30px;
  }
  .brand-band .wordmark { font-size: 42px; color: #fff; letter-spacing: 1px; }
  .grey-band {
    position: absolute; left: 0; top: 186px;
    width: 282px; height: 14px; background: var(--band-grey);
  }
  .divider {
    position: absolute; left: 290px; top: 82px;
    width: 2px; height: 196px; background: var(--lime);
  }
  .details {
    position: absolute; left: 306px; top: 72px; width: 200px;
    color: var(--ink); white-space: nowrap;
  }
  .holder-name { font-size: 16px; letter-spacing: 0.6px; text-transform: uppercase; margin-bottom: 8px; }
  .contact-list { list-style: none; }
  .contact-list li {
    display: flex; align-items: center; gap: 6px;
    font-size: 12.5px; line-height: 19px; color: var(--ink-soft);
  }
  .contact-list svg { width: 13px; height: 13px; flex: none; }
  .address { margin-top: 14px; font-size: 12.5px; line-height: 16px; color: var(--ink-soft); }
</style>
</head>
<body>
<div class="stage">
  <section class="card card-back">
    <span class="wordmark">Veltora</span>
  </section>

  <section class="card card-front">
    <div class="brand-band"><span class="wordmark">Veltora</span></div>
    <div class="grey-band"></div>
    <div class="divider"></div>
    <div class="details">
      <p class="holder-name">Marten Kuyvelsma</p>
      <ul class="contact-list">
        <li>
          <svg viewBox="0 0 14 14"><circle cx="7" cy="7" r="6.2" fill="none" stroke="#9db31b" stroke-width="1.2"/><rect x="5" y="3.3" width="4" height="7.4" rx="0.8" fill="none" stroke="#9db31b" stroke-width="1"/></svg>
          +31 6 927 15 062
        </li>
        <li>
          <svg viewBox="0 0 14 14"><circle cx="7" cy="7" r="6.2" fill="none" stroke="#9db31b" stroke-width="1.2"/><path d="M4.4 4.2c.4-.4.9-.4 1.1 0l.6 1.1c.2.3 0 .6-.2.8l-.3.3c.4.9 1.1 1.6 2 2l.3-.3c.2-.2.5-.4.8-.2l1.1.6c.4.2.4.7 0 1.1-.6.6-1.4.8-2.2.4-1.6-.8-2.8-2-3.6-3.6-.4-.8-.2-1.6.4-2.2z" fill="#9db31b"/></svg>
          +31 255 47 09 36
        </li>
        <li>
          <svg viewBox="0 0 14 14"><circle cx="7" cy="7" r="6.2" fill="none" stroke="#9db31b" stroke-width="1.2"/><rect x="3.8" y="4.8" width="6.4" height="4.4" fill="none" stroke="#9db31b" stroke-width="1"/><path d="M3.8 4.8 7 7.3l3.2-2.5" fill="none" stroke="#9db31b" stroke-width="1"/></svg>
          marten@veltora-demo.com
        </li>
        <li>
          <svg viewBox="0 0 14 14"><circle cx="7" cy="7" r="6.2" fill="none" stroke="#9db31b" stroke-width="1.2"/><circle cx="7" cy="7" r="3.6" fill="none" stroke="#9db31b" stroke-width="0.9"/><path d="M3.4 7h7.2M7 3.4v7.2M7 3.4c-1.6 2-1.6 5.2 0 7.2M7 3.4c1.6 2 1.6 5.2 0 7.2" fill="none" stroke="#9db31b" stroke-width="0.8"/></svg>
          www.veltora-demo.com
        </li>
        <li>
          <svg viewBox="0 0 14 14"><circle cx="7" cy="7" r="6.2" fill="none" stroke="#9db31b" stroke-width="1.2"/></svg>
          /VeltoraHQ
        </li>
        <li>
          <svg viewBox="0 0 14 14"><circle cx="7" cy="7" r="6.2" fill="none" stroke="#9db31b" stroke-width="1.2"/></svg>
          /VeltoraApp
        </li>
      </ul>
      <p class="address">Oostelingpad 84c<br>2184 KT Lindervaart</p>
    </div>
  </section>
</div>
</body>
</html>
```